TLR Property - Business Cards

Looking for a business card & general letterhead, signage etc design for our new logo.

Colours:
000a20
0056a2
00b5ef
0088ce
68cef2

Fonts:
Poppins
Karla

Please keep look and feel of new brand - example in the zip package I sent.

```html
<!DOCTYPE html>
<html lang="en">
<head>
<meta charset="utf-8">
<title>TLR Property – Business Cards</title>
<link href="https://fonts.googleapis.com/css2?family=Montserrat:wght@400;500;700&display=swap" rel="stylesheet">
<style>
  :root {
    --bg: #2b2b2b;
    --navy: #0f1428;
    --navy-deep: #000a20;
    --blue: #0056a2;
    --blue-mid: #0088ce;
    --cyan: #00b5ef;
    --sky: #68cef2;
    --ink-soft: #1b2a5c;
    --white: #ffffff;
  }
  * { margin: 0; padding: 0; box-sizing: border-box; }
  html, body { width: 1200px; height: 689px; overflow: hidden; }
  body {
    background: var(--bg);
    font-family: "Montserrat", sans-serif;
    display: flex;
    align-items: center;
    justify-content: center;
    gap: 50px;
  }
  .card {
    position: relative;
    width: 530px;
    height: 304px;
    border-radius: 22px;
    background: var(--navy);
    overflow: hidden;
  }
  /* back */
  .card-back { display: flex; align-items: center; justify-content: center; }
  .brand { display: flex; align-items: center; gap: 14px; }
  .brand-dot { width: 34px; height: 34px; border-radius: 50%; }
  .brand-name { font-weight: 700; font-size: 46px; letter-spacing: 1px; line-height: 1; }
  .card-back .brand-dot { background: var(--ink-soft); }
  .card-back .brand-name { color: var(--ink-soft); }
  /* front */
  .card-front .brand { position: absolute; top: 34px; right: 32px; }
  .card-front .brand-dot { background: var(--cyan); width: 26px; height: 26px; }
  .card-front .brand-name { color: var(--blue); font-size: 32px; }
  .holder { position: absolute; left: 34px; top: 118px; }
  .holder-name { color: var(--blue); font-weight: 700; font-size: 22px; letter-spacing: 0.5px; }
  .holder-role { color: var(--white); font-weight: 400; font-size: 13px; letter-spacing: 1px; margin-top: 4px; }
  .rule { position: absolute; left: 34px; right: 32px; top: 178px; height: 1px; background: var(--white); }
  .contacts { position: absolute; left: 34px; top: 192px; list-style: none; }
  .contacts li { display: flex; align-items: center; gap: 10px; color: var(--white); font-size: 13px; line-height: 16px; margin-bottom: 8px; }
  .contacts svg { width: 15px; height: 15px; flex: none; }
  .address { position: absolute; right: 32px; top: 196px; color: var(--white); font-size: 13px; text-align: right; line-height: 1.6; }
  .band { position: absolute; left: 0; right: 0; bottom: 0; height: 8px; display: flex; }
  .band-a { flex: 5; background: var(--blue); }
  .band-b { flex: 5; background: var(--sky); }
  .band-c { flex: 3; background: var(--blue-mid); }
</style>
</head>
<body>
  <section class="card card-back" aria-label="Card back">
    <div class="brand">
      <span class="brand-dot"></span>
      <span class="brand-name">TLR Property</span>
    </div>
  </section>

  <section class="card card-front" aria-label="Card front">
    <div class="brand">
      <span class="brand-dot"></span>
      <span class="brand-name">TLR Property</span>
    </div>
    <div class="holder">
      <p class="holder-name">DANIEL HART</p>
      <p class="holder-role">MANAGING DIRECTOR</p>
    </div>
    <div class="rule"></div>
    <ul class="contacts">
      <li>
        <svg viewBox="0 0 24 24" fill="var(--blue-mid)"><path d="M6.6 10.8a15 15 0 0 0 6.6 6.6l2.2-2.2a1 1 0 0 1 1-.25 11.4 11.4 0 0 0 3.6.57 1 1 0 0 1 1 1V20a1 1 0 0 1-1 1A17 17 0 0 1 3 4a1 1 0 0 1 1-1h3.5a1 1 0 0 1 1 1c0 1.25.2 2.45.57 3.57a1 1 0 0 1-.25 1z"/></svg>
        044-555 018 240
      </li>
      <li>
        <svg viewBox="0 0 24 24" fill="none" stroke="var(--blue-mid)" stroke-width="2"><rect x="3" y="5" width="18" height="14" rx="1"/><path d="M3 6l9 7 9-7"/></svg>
        hello@tlrproperty.com
      </li>
      <li>
        <svg viewBox="0 0 24 24" fill="none" stroke="var(--blue-mid)" stroke-width="2"><circle cx="12" cy="12" r="9"/><path d="M3 12h18M12 3c3 3 3 15 0 18M12 3c-3 3-3 15 0 18"/></svg>
        www.tlrproperty.com
      </li>
    </ul>
    <p class="address">27 Harbour Lane, Suite 4<br>30918, Northbridge</p>
    <div class="band"><span class="band-a"></span><span class="band-b"></span><span class="band-c"></span></div>
  </section>
</body>
</html>
```